Stationary Design for Norvath Digital

We are after a full stationary back business cards, letterheads, compliment slip, invoice template, delivery note and anything else we could use within the stationary pack.

We would also like an email footer creating.

Our company details to be included on all stationary:

Registered Name: Norvath Limited
Company Registration Number: 20473915
Website: www.norvathdigital.example
email: info@norvathdigital.example
Phone: 01632 960 417
Address: 48 Tamsin Lane Harrowfield Marlshire United Kingdom HF4 9QX

```html
<!DOCTYPE html>
<html lang="en">
<head>
<meta charset="utf-8">
<title>Delivery Note – Norvath Digital</title>
<link href="https://fonts.googleapis.com/css2?family=Bebas+Neue&family=Didact+Gothic&family=Arimo:ital,wght@0,700;1,400;1,700&display=swap" rel="stylesheet">
<style>
  :root {
    --ink: #111111;
    --paper: #ffffff;
    --gold: #e3cd1f;
    --gold-light: #efe27a;
    --header-blue: #b1cfe9;
    --qty-green: #bde0c9;
    --arrow-edge: #587b92;
    --label-ink: #1d2a33;
  }
  html, body {
    margin: 0;
    width: 1033px;
    height: 1200px;
    overflow: hidden;
    background: var(--paper);
  }
  .canvas {
    position: relative;
    width: 1033px;
    height: 1200px;
    color: var(--ink);
    font-family: "Didact Gothic", sans-serif;
  }
  .band {
    position: absolute;
    top: 115px;
    height: 15px;
    background: linear-gradient(180deg, var(--gold-light), var(--gold) 60%);
  }
  .band--left { left: 0; width: 420px; }
  .band--right { left: 651px; width: 382px; }
  .doc-title {
    position: absolute;
    top: 100px;
    left: 420px;
    width: 231px;
    margin: 0;
    text-align: center;
    font-family: "Bebas Neue", sans-serif;
    font-weight: 400;
    font-size: 44px;
    line-height: 48px;
    letter-spacing: 0.3px;
  }
  .frame {
    position: absolute;
    left: 69px;
    top: 160px;
    width: 909px;
    height: 975px;
    border: 4px solid var(--ink);
    border-radius: 2px;
  }
  .address-tag {
    position: absolute;
    left: 94px;
    top: 203px;
    width: 504px;
    height: 186px;
  }
  .address-tag__label {
    position: absolute;
    left: 122px;
    top: 230px;
    font-family: "Arimo", sans-serif;
    font-style: italic;
    font-size: 15px;
    color: var(--label-ink);
  }
  .brand {
    position: absolute;
    left: 660px;
    top: 224px;
    width: 290px;
    text-align: center;
    font-size: 35px;
    line-height: 44px;
    letter-spacing: 1px;
  }
  .contact {
    position: absolute;
    left: 660px;
    top: 305px;
    width: 276px;
    text-align: center;
    font-size: 11.5px;
    line-height: 14px;
  }
  .contact p { margin: 0; }
  .contact .gap { margin-top: 15px; }
  table { border-collapse: collapse; position: absolute; }
  th {
    font-family: "Bebas Neue", sans-serif;
    font-weight: 400;
    font-size: 22px;
    background: var(--header-blue);
    padding: 0;
  }
  th, td { border: 2px solid var(--ink); padding: 0; }
  .dispatch-table { left: 97px; top: 411px; width: 853px; }
  .dispatch-table th { height: 36px; }
  .dispatch-table td { height: 56px; }
  .section-label {
    position: absolute;
    left: 101px;
    top: 533px;
    margin: 0;
    font-family: "Arimo", sans-serif;
    font-style: italic;
    font-weight: 700;
    font-size: 17px;
  }
  .items-table { left: 99px; top: 558px; width: 851px; }
  .items-table th { height: 43px; }
  .items-table td.qty { background: var(--qty-green); width: 141px; }
  .received {
    position: absolute;
    left: 100px;
    top: 996px;
    margin: 0;
    font-family: "Arimo", sans-serif;
    font-weight: 700;
    font-size: 17.5px;
  }
  .claims {
    position: absolute;
    left: 560px;
    top: 999px;
    width: 400px;
    margin: 0;
    font-family: "Arimo", sans-serif;
    font-weight: 700;
    font-size: 13.8px;
    line-height: 16.5px;
  }
  .signoff {
    position: absolute;
    top: 1092px;
    border-top: 2px solid var(--ink);
    padding-top: 5px;
    text-align: center;
    font-family: "Arimo", sans-serif;
    font-weight: 700;
    font-size: 14px;
  }
  .signoff--signature { left: 103px; width: 315px; }
  .signoff--name { left: 451px; width: 269px; }
  .signoff--date { left: 743px; width: 205px; }
</style>
</head>
<body>
<div class="canvas">
  <div class="band band--left"></div>
  <h1 class="doc-title">Delivery Note</h1>
  <div class="band band--right"></div>

  <div class="frame"></div>

  <svg class="address-tag" viewBox="0 0 504 186" aria-hidden="true">
    <defs>
      <linearGradient id="tagFill" x1="0" y1="0" x2="1" y2="1">
        <stop offset="0" stop-color="#6a8fa8"/>
        <stop offset="1" stop-color="#85a4b8"/>
      </linearGradient>
    </defs>
    <path d="M36 2 L36 12 L418 12 L498 92 L418 172 L36 172 L36 184 L2 172 L2 12 Z" fill="var(--arrow-edge)"/>
    <path d="M14 16 L418 16 L492 92 L418 166 L14 166 Z" fill="url(#tagFill)"/>
  </svg>
  <div class="address-tag__label">DELIVERY ADDRESS</div>

  <div class="brand">Norvath Digital</div>
  <div class="contact">
    <p>48 Tamsin Lane Harrowfield</p>
    <p>Marlshire United Kingdom, HF4 9QX</p>
    <p class="gap">phone: 01632 960 417</p>
    <p>info@norvathdigital.example</p>
    <p>www.norvathdigital.example</p>
    <p>Company Reg #: 20473915</p>
  </div>

  <table class="dispatch-table">
    <tr>
      <th style="width:160px">Dispatch Date</th>
      <th style="width:120px">Order No.</th>
      <th style="width:120px">Reference No.</th>
      <th style="width:277px">Delivery Method</th>
      <th>Delivery Note No.</th>
    </tr>
    <tr><td></td><td></td><td></td><td></td><td></td></tr>
  </table>

  <p class="section-label">PLEASE RECIEVE THE FOLLOWING:</p>

  <table class="items-table">
    <tr><th style="width:141px">Quantity</th><th>Description</th></tr>
    <tr style="height:56px"><td class="qty"></td><td></td></tr>
    <tr style="height:53px"><td class="qty"></td><td></td></tr>
    <tr style="height:59px"><td class="qty"></td><td></td></tr>
    <tr style="height:55px"><td class="qty"></td><td></td></tr>
    <tr style="height:54px"><td class="qty"></td><td></td></tr>
    <tr style="height:54px"><td class="qty"></td><td></td></tr>
    <tr style="height:55px"><td class="qty"></td><td></td></tr>
  </table>

  <p class="received">RECEIVED IN GOOD CONDITION</p>
  <p class="claims">CLAIMS FOR NON-DELIVERY, PART DELIVERY OR<br>DAMAGE MUST BE ADVISED IN WRITING WITHIN 3 DAYS<br>OF DISPATCH DATE</p>

  <div class="signoff signoff--signature">SIGNATURE</div>
  <div class="signoff signoff--name">NAME</div>
  <div class="signoff signoff--date">DATE</div>
</div>
</body>
</html>
```